Meadow Lantern Veterinary Practice including Nest2Grow

We require a double-sided full colour tri-fold Brochure for Print.
Colour theme to in line with logo below

Written CONTENT below
Orphans
We can provide care and a new mother for orphan foals of any age, breed or size, from thoroughbreds and draft breeds to tiny ponies and even donkeys.
We have successfully fostered orphans from a few hours of age through to eight weeks, regardless of how long or if at all they were with their birth mother, and of previous fostering attempts.
We have the knowledge and experience to provide optimum nutrition and care to orphans during the brief period that they don’t have a mum, until their new foster mother is ready to take them.
Additionally we are a veterinary practice, and can provide diagnostics and therapeutics for compromised orphan foals such as plasma administration and health checks.

Mares
Nest2Grow mares have been selected for mothering ability and temperament, and have all carried and raised at least one foal of their own. Many have already been successful foster mothers in one or more of the last five breeding seasons.
The mares are not currently pregnant and are given a carefully designed course of hormones to induce lactation when required. The milk produced is not colostrum, but is completely normal and equivalent to that which they would have had if the foal was theirs by birth.
There is published scientific information (in addition to our own experience and that of the owners of previous graduates of our programme) that growth and development of foals raised by induced lactation is identical to that of foals raised by their birth mothers.

Fostering
During the few days when the mare’s udder is developing, mare and foal are kept next separately but in close proximity, allowing bonding to begin and reducing stress on the orphan.
The fostering is completed once the mare has enough milk to feed the foal, and our experienced handlers ensure that joining the two goes smoothly.
Once they are together the mare completely accepts the foal as her own, and the foal can suckle freely – at this stage we continue to offer supplementary feeds until they are not needed.
The mare and foal are then a normal unit and can return to the foal owner’s care until weaning – ensuring optimum nutrition and behaviour for the foal and excellent outcomes in performance, relationships with other horses, and interaction with humans.

Complete Safety
Mares recognise their birth foal by scent - a unique bond established during the first few minutes of the foal’s life - and only a small percentage of mares who have lost their own foal will readily accept a substitute.
When a mare who has lost her birth foal is offered an orphan, it is very normal and common for her to respond with aggression - to the danger of the foal and the human handler.
Nest2Grow mares have no birth foal in the current season, and are happy to adopt any foal who is placed close to them during the hormone treatment period.
This makes for total foal and handler safety.

Excellent Success Rate
After seven years of perfecting the fostering method, Nest2Grow can claim total success: we have now documented almost 50 fosterings over the last five breeding seasons. We have never been entrusted with an orphan foal that we have not been able to provide with a beautiful foster mum.

Career Mothers
Being dedicated career mothers with no other job in life, our mares are free to accompany their new foals home and stay with them as long as required. No foals are weaned and left without a mother in our programme, and our beautiful mares who would otherwise not be bred, are given a foal every year and a wonderful lifelong purpose.

Every single orphan’s human family has admired and appreciated our beautiful mares, with many offering to give them a home for life. Each season as the orphans are weaned, we welcome our mares home to Meadow Lantern to prepare for the next foal in need – a job they totally love! – just as if they were in a natural breeding situation.

Meadow Lantern Vet Practice including Nest2Grow
214 Pellerby Lane
Thornvale. Vic. 3812

Phone 0431958617 or 0419284056

```html
<!DOCTYPE html>
<html lang="en">
<head>
<meta charset="utf-8">
<title>Meadow Lantern Veterinary Practice – Nest2Grow Brochure</title>
<link rel="stylesheet" href="https://fonts.googleapis.com/css2?family=Oswald:wght@500;600&family=Open+Sans:wght@400;600&display=swap">
<style>
:root{
  --backdrop:#e8d8ca;
  --peach:#f6c29c;
  --peach-deep:#eab089;
  --red:#e33b32;
  --red-dark:#c92b24;
  --white:#ffffff;
  --ink:#3a2418;
  --photo-a:#6f5a45;
  --photo-b:#3f4a2e;
  --photo-c:#9a8a72;
}
*{box-sizing:border-box;margin:0;padding:0}
html,body{width:931px;height:1200px;overflow:hidden}
body{background:var(--backdrop);font-family:"Open Sans",Arial,sans-serif;color:var(--ink);position:relative}
.sheet{position:absolute;left:20px;width:891px;height:540px;overflow:hidden;box-shadow:0 6px 18px rgba(80,50,30,.18)}
.sheet--outside{top:30px}
.sheet--inside{top:630px}
.sheet__art{position:absolute;inset:0}
.copy{position:absolute;font-size:8.6px;line-height:11.4px;text-align:justify}
.copy p{margin-bottom:5px}
.copy--light{color:var(--white)}
.heading{font-family:"Oswald",Arial,sans-serif;font-weight:600;font-size:19px;line-height:22px;color:var(--red);text-transform:uppercase;margin-bottom:4px}
.copy--light .heading{color:var(--white)}
.success{position:absolute;left:316px;top:112px;width:188px;text-align:center;font-size:8.4px;line-height:11px}
.success .heading{font-size:18px;line-height:19px;margin-bottom:5px}
.brand{display:flex;align-items:center;gap:6px;font-family:"Open Sans",Arial,sans-serif;font-weight:600;color:var(--red);position:absolute}
.brand__dot{width:12px;height:12px;border-radius:50%;background:var(--red)}
.brand--top{left:632px;top:12px;font-size:17px}
.brand--contact{left:320px;top:398px;font-size:15px}
.headline{position:absolute;left:640px;top:92px;font-family:"Oswald",Arial,sans-serif;font-weight:500;color:var(--red);text-transform:uppercase;line-height:.95}
.headline__line{display:block}
.headline__line--sm{font-size:26px;padding-left:10px}
.headline__line--md{font-size:40px;padding-left:38px}
.headline__line--lg{font-size:58px;padding-left:42px;font-weight:600}
.contact{position:absolute;left:322px;top:440px;color:var(--white);font-size:10.5px;line-height:15px}
.contact__row{display:flex;align-items:flex-start;gap:7px;margin-bottom:4px}
.contact__row svg{flex:none;margin-top:2px}
.orphans-copy{left:16px;top:254px;width:262px}
.mares-copy{left:312px;top:274px;width:266px}
.fostering-copy{left:610px;top:184px;width:266px}
</style>
</head>
<body>

<section class="sheet sheet--outside" aria-label="Brochure outside">
  <svg class="sheet__art" width="891" height="540" viewBox="0 0 891 540">
    <defs>
      <linearGradient id="photoMare" x1="0" y1="0" x2="1" y2="1">
        <stop offset="0" stop-color="var(--photo-c)"/><stop offset=".5" stop-color="var(--photo-a)"/><stop offset="1" stop-color="#8a8f6a"/>
      </linearGradient>
      <linearGradient id="photoHandler" x1="0" y1="0" x2="0" y2="1">
        <stop offset="0" stop-color="#55603f"/><stop offset=".6" stop-color="var(--photo-a)"/><stop offset="1" stop-color="#6f9a45"/>
      </linearGradient>
    </defs>
    <rect width="891" height="540" fill="var(--peach)"/>
    <rect x="0" y="250" width="297" height="290" fill="var(--peach-deep)"/>
    <rect x="297" width="297" height="540" fill="var(--red)"/>
    <path d="M0 0H440V120Q330 230 120 250Q50 256 0 252Z" fill="url(#photoMare)" stroke="var(--white)" stroke-width="5" role="img" aria-label="Photo: a bay mare lying in grass nuzzling her young foal"/>
    <path d="M594 0H891V40Q780 78 620 66Q604 64 594 58Z" fill="var(--white)"/>
    <path d="M300 388Q440 360 594 382V420Q440 404 300 430Z" fill="var(--white)"/>
    <path d="M594 540V360Q610 235 735 205Q830 184 891 200V540Z" fill="url(#photoHandler)" stroke="var(--white)" stroke-width="6" role="img" aria-label="Photo: a woman standing with a dark mare and a pale foal in a paddock"/>
    <circle cx="410" cy="200" r="112" fill="var(--peach)" stroke="var(--white)" stroke-width="6"/>
  </svg>

  <div class="copy" style="left:16px;top:262px;width:268px">
    <h2 class="heading">Career Mothers</h2>
    <p>Being dedicated career mothers with no other job in life, our mares are free to accompany their new foals home and stay with them as long as required. No foals are weaned and left without a mother in our programme, and our beautiful mares who would otherwise not be bred, are given a foal every year and a wonderful lifelong purpose.</p>
    <p>Every single orphan’s human family has admired and appreciated our beautiful mares, with many offering to give them a home for life. Each season as the orphans are weaned, we welcome our mares home to Meadow Lantern to prepare for the next foal in need – a job they totally love! – just as if they were in a natural breeding situation.</p>
  </div>

  <div class="success">
    <h2 class="heading">Excellent<br>Success Rate</h2>
    <p>After seven years of perfecting the fostering method, Nest2Grow can claim total success: we have now documented almost 50 fosterings over the last five breeding seasons. We have never been entrusted with an orphan foal that we have not been able to provide with a beautiful foster mum.</p>
  </div>

  <div class="brand brand--contact"><span class="brand__dot"></span>Meadow Lantern</div>
  <div class="contact">
    <div class="contact__row">
      <svg width="10" height="13" viewBox="0 0 10 13"><path d="M5 0a5 5 0 0 0-5 5c0 3.6 5 8 5 8s5-4.4 5-8a5 5 0 0 0-5-5zm0 7a2 2 0 1 1 0-4 2 2 0 0 1 0 4z" fill="var(--peach)"/></svg>
      <span>214 Pellerby Lane<br>Thornvale. Vic. 3812</span>
    </div>
    <div class="contact__row">
      <svg width="11" height="11" viewBox="0 0 11 11"><path d="M2.3 0.5l1.8 2.2-1 1.3a7 7 0 0 0 3.9 3.9l1.3-1 2.2 1.8-1 1.8C5 10.5.5 6 .5 1.5z" fill="var(--peach)"/></svg>
      <span>0431958617 or 0419284056</span>
    </div>
  </div>

  <div class="brand brand--top"><span class="brand__dot"></span>Meadow Lantern</div>
  <h1 class="headline">
    <span class="headline__line headline__line--sm">A Job They</span>
    <span class="headline__line headline__line--md">Totally</span>
    <span class="headline__line headline__line--lg">Love!</span>
  </h1>
</section>

<section class="sheet sheet--inside" aria-label="Brochure inside">
  <svg class="sheet__art" width="891" height="540" viewBox="0 0 891 540">
    <defs>
      <linearGradient id="photoOrphan" x1="0" y1="0" x2="1" y2="1">
        <stop offset="0" stop-color="var(--photo-b)"/><stop offset=".55" stop-color="#5a3a2c"/><stop offset="1" stop-color="#7a8a55"/>
      </linearGradient>
      <linearGradient id="photoFoster" x1="0" y1="0" x2="1" y2="0">
        <stop offset="0" stop-color="#7a4630"/><stop offset="1" stop-color="#3e5a2e"/>
      </linearGradient>
    </defs>
    <rect width="891" height="540" fill="var(--peach)"/>
    <rect x="297" width="297" height="540" fill="var(--red)"/>
    <path d="M0 0H600V170Q470 262 300 262Q140 262 0 200Z" fill="url(#photoOrphan)" stroke="var(--white)" stroke-width="6" role="img" aria-label="Photo: a woman helping a bay mare meet a newborn dark foal beside a paddock fence"/>
    <path d="M594 0H891V110Q760 128 600 168Z" fill="url(#photoFoster)" stroke="var(--white)" stroke-width="5" role="img" aria-label="Photo: a young woman with a chestnut mare and her foster foal"/>
  </svg>

  <div class="copy orphans-copy">
    <h2 class="heading">Orphans</h2>
    <p>We can provide care and a new mother for orphan foals of any age, breed or size, from thoroughbreds and draft breeds to tiny ponies and even donkeys.</p>
    <p>We have successfully fostered orphans from a few hours of age through to eight weeks, regardless of how long or if at all they were with their birth mother, and of previous fostering attempts.</p>
    <p>We have the knowledge and experience to provide optimum nutrition and care to orphans during the brief period that they don’t have a mum, until their new foster mother is ready to take them.</p>
  </div>

  <div class="copy copy--light mares-copy">
    <p>Additionally we are a veterinary practice, and can provide diagnostics and therapeutics for compromised orphan foals such as plasma administration and health checks.</p>
    <h2 class="heading">Mares</h2>
    <p>Nest2Grow mares have been selected for mothering ability and temperament, and have all carried and raised at least one foal of their own. Many have already been successful foster mothers in one or more of the last five breeding seasons.</p>
    <p>The mares are not currently pregnant and are given a carefully designed course of hormones to induce lactation when required. The milk produced is not colostrum, but is completely normal and equivalent to that which they</p>
  </div>

  <div class="copy fostering-copy">
    <p>would have had if the foal was theirs by birth.</p>
    <p>There is published scientific information (in addition to our own experience and that of the owners of previous graduates of our programme) that growth and development of foals raised by induced lactation is identical to that of foals raised by their birth mothers.</p>
    <h2 class="heading">Fostering</h2>
    <p>During the few days when the mare’s udder is developing, mare and foal are kept next separately but in close proximity, allowing bonding to begin and reducing stress on the orphan.</p>
    <p>The fostering is completed once the mare has enough milk to feed the foal, and our experienced handlers ensure that joining the two goes smoothly.</p>
    <p>Once they are together the mare completely accepts the foal as her own, and the foal can suckle freely – at this stage we continue to offer supplementary feeds until they are not needed.</p>
    <p>The mare and foal are then a normal unit and can return to the foal owner’s care until weaning – ensuring optimum nutrition and behaviour for the foal and excellent outcomes in performance, relationships with other horses, and interaction with humans.</p>
  </div>
</section>

</body>
</html>
```